B7k Website Design

We need a website design, look, feel and functionality that uses a recently approved logo attached. This should be a highly professional looking website that is relatively simple, but scalable. The website should carry information about the company, links and blog posts. The look and feel of the website should be consistent with the logo colour palette, but does not have to stick to them exactly. The company provides high quality brokering and support services for multinational companies to work with international humanitarian organisations and the Meridian Accord. Where possible, the design should make the most of the concept that collective action has a greater impact, and that Compass9Reach can help make that happen. The attached text can be used as a basis for the website text.

Target Market(s)

Heads of company foundations, and humanitarian organisations, and Meridian Accord departments the promote collaboration

Number of Pages Required

3 page

Requirements
Should not have
• Photos of people in suits.
• Photos of poor African children begging for help, or smiling in gratitude for aid

```html
<!DOCTYPE html>
<html lang="en">
<head>
<meta charset="utf-8">
<title>Compass9Reach (B7k)</title>
<link rel="stylesheet" href="https://fonts.googleapis.com/css2?family=Roboto:wght@300;400;500;700&family=Roboto+Condensed:wght@400;700&family=Muli:wght@400;600&display=swap">
<style>
  :root {
    --accent: #ff5a36;
    --accent-dark: #f04e2b;
    --brand-blue: #3b44d6;
    --ink: #222428;
    --body: #3a3d42;
    --muted: #8a8d93;
    --white: #ffffff;
    --footer-bg: #eef1f5;
    --rule: #e6e8eb;
    --violet: rgba(104, 96, 245, 0.72);
  }
  * { margin: 0; padding: 0; box-sizing: border-box; }
  html, body { width: 1200px; height: 2434px; overflow: hidden; }
  body { position: relative; font-family: "Roboto", Arial, sans-serif; color: var(--body); background: var(--white); }
  a { color: inherit; text-decoration: none; }
  .abs { position: absolute; }

  /* Header */
  .site-header { position: absolute; left: 0; top: 0; width: 1200px; height: 80px; background: var(--white); }
  .brand { position: absolute; left: 124px; top: 22px; display: flex; align-items: center; gap: 8px; }
  .brand-dot { width: 38px; height: 38px; border-radius: 50%; border: 3px solid var(--accent); }
  .brand-name { font-family: "Roboto", Arial, sans-serif; font-weight: 500; font-size: 25px; color: var(--brand-blue); letter-spacing: -0.2px; }
  .main-nav { position: absolute; left: 458px; top: 38px; display: flex; font-family: "Roboto Condensed", Arial, sans-serif; font-size: 16px; color: var(--ink); }
  .main-nav a { margin-right: 23px; position: relative; }
  .main-nav a.is-current { color: var(--accent); }
  .main-nav a.is-current::after { content: ""; position: absolute; left: 0; right: 0; top: 26px; height: 2px; background: var(--accent); }
  .btn { display: inline-flex; align-items: center; justify-content: center; background: var(--accent); color: var(--white); font-weight: 500; border-radius: 2px; }
  .btn-donate { position: absolute; left: 965px; top: 29px; width: 111px; height: 35px; font-size: 14px; font-family: "Roboto Condensed", Arial, sans-serif; }

  /* Hero */
  .hero { position: absolute; left: 0; top: 80px; width: 1200px; height: 440px;
    background: linear-gradient(180deg, #6c7a86 0%, #7e8a62 30%, #5f6b3a 55%, #7a705e 80%, #8a7f70 100%); }
  .hero-shade { position: absolute; inset: 0; background: rgba(0,0,0,0.22); }
  .hero-title { position: absolute; left: 0; width: 1200px; top: 155px; text-align: center; color: var(--white); font-size: 47px; font-weight: 700; font-family: "Roboto Condensed", Arial, sans-serif; }
  .hero-sub { position: absolute; left: 320px; width: 560px; top: 208px; text-align: center; color: var(--white); font-size: 15px; line-height: 19px; }
  .btn-hero { position: absolute; left: 540px; top: 257px; width: 120px; height: 33px; font-size: 14px; }

  /* Welcome */
  .welcome-kicker { top: 556px; left: 0; width: 1200px; text-align: center; font-size: 22px; color: var(--ink); }
  .welcome-title { top: 592px; left: 0; width: 1200px; text-align: center; font-size: 38px; font-weight: 700; color: var(--accent); font-family: "Roboto Condensed", Arial, sans-serif; }
  .welcome-text { top: 648px; left: 185px; width: 830px; text-align: center; font-size: 15px; line-height: 26px; color: var(--ink); }
  .welcome-link { top: 750px; left: 0; width: 1200px; text-align: center; font-size: 15px; font-weight: 500; color: var(--accent); }

  /* Volunteers */
  .volunteer-band { position: absolute; left: 0; top: 806px; width: 1200px; height: 373px;
    background: linear-gradient(90deg, #8d8fd8 0%, #9e8ee0 40%, #b6a2d8 70%, #9a92e0 100%); }
  .volunteer-band .overlay { position: absolute; inset: 0; background: var(--violet); }
  .kicker { left: 0; width: 1200px; text-align: center; color: var(--white); font-size: 22px; }
  .kicker-rule { left: 520px; width: 145px; height: 3px; background: var(--accent); }
  .volunteer-title { top: 920px; left: 0; width: 1200px; text-align: center; color: var(--white); font-size: 51px; font-weight: 700; font-family: "Roboto Condensed", Arial, sans-serif; }
  .volunteer-text { top: 982px; left: 290px; width: 620px; text-align: center; color: var(--white); font-size: 22px; line-height: 34px; }
  .btn-signup { position: absolute; left: 540px; top: 1077px; width: 122px; height: 34px; font-size: 14px; }

  /* News */
  .section-title { top: 1252px; left: 0; width: 1200px; text-align: center; font-size: 30px; font-weight: 700; color: var(--ink); }
  .section-rule { top: 1289px; left: 518px; width: 162px; height: 3px; background: var(--accent); }
  .news-card { position: absolute; top: 1317px; width: 250px; height: 305px; background: var(--white); }
  .news-card .thumb { width: 250px; height: 138px; }
  .news-card .date { position: absolute; left: 26px; top: 155px; font-family: "Muli", Arial, sans-serif; font-size: 9px; color: var(--muted); letter-spacing: 0.3px; }
  .news-card .title { position: absolute; left: 26px; top: 175px; font-family: "Muli", Arial, sans-serif; font-size: 14px; color: var(--ink); }
  .news-card .excerpt { position: absolute; left: 26px; top: 203px; width: 210px; font-family: "Muli", Arial, sans-serif; font-size: 10px; line-height: 16px; color: var(--muted); }
  .news-card .divider { position: absolute; left: 0; top: 268px; width: 250px; height: 1px; background: var(--rule); }
  .news-card .more { position: absolute; left: 24px; top: 284px; font-size: 12px; font-weight: 500; color: var(--accent); }
  .news-card.bordered { border-left: 1px solid var(--rule); }

  /* Gallery */
  .gallery { position: absolute; left: 0; top: 1686px; width: 1200px; height: 175px; display: flex; }
  .gallery .tile { width: 200px; height: 175px; }
  .to-top { position: absolute; left: 1152px; top: 1792px; width: 32px; height: 32px; border-radius: 50%; background: rgba(120,120,120,0.75); }

  /* Newsletter */
  .newsletter { position: absolute; left: 0; top: 1886px; width: 1200px; height: 282px;
    background: linear-gradient(90deg, #5a5b4c 0%, #6e6650 35%, #7a6a5c 60%, #8a6f6e 100%); }
  .newsletter .overlay { position: absolute; inset: 0; background: rgba(20,20,20,0.35); }
  .newsletter-title { top: 1936px; left: 0; width: 1200px; text-align: center; color: var(--white); font-size: 31px; font-weight: 500; }
  .newsletter-text { top: 1980px; left: 0; width: 1200px; text-align: center; color: var(--white); font-size: 15px; line-height: 25px; }
  .signup-field { position: absolute; left: 401px; top: 2048px; width: 293px; height: 43px; background: var(--white); border-radius: 3px 0 0 3px; padding-left: 20px; display: flex; align-items: center; font-size: 15px; color: var(--muted); }
  .signup-btn { position: absolute; left: 694px; top: 2048px; width: 111px; height: 43px; font-size: 16px; border-radius: 0 3px 3px 0; }

  /* Footer */
  .site-footer { position: absolute; left: 0; top: 2168px; width: 1200px; height: 266px; background: var(--footer-bg); }
  .footer-dot { position: absolute; left: 282px; top: 2250px; width: 56px; height: 56px; border-radius: 50%; border: 4px solid var(--accent); }
  .footer-name { top: 2322px; left: 200px; width: 220px; text-align: center; font-size: 29px; font-weight: 500; color: var(--brand-blue); letter-spacing: -0.3px; }
  .footer-col { position: absolute; top: 2218px; font-size: 14px; color: var(--ink); }
  .footer-col h4 { font-size: 14px; font-weight: 700; margin-bottom: 10px; }
  .footer-col li { list-style: none; line-height: 29.5px; }
  .footer-col li.is-current { color: var(--accent); }
  .social { position: absolute; left: 826px; top: 2262px; display: flex; gap: 5px; }
  .social span { width: 28px; height: 28px; border-radius: 50%; background: #dcdfe4; }
  .copyright { top: 2364px; left: 722px; font-size: 12px; color: var(--muted); }
  .copyright b { font-weight: 400; color: var(--accent); }
</style>
</head>
<body>

<header class="site-header">
  <a class="brand" href="#"><span class="brand-dot"></span><span class="brand-name">Compass9Reach</span></a>
  <nav class="main-nav">
    <a class="is-current" href="#">HOME</a>
    <a href="#">ABOUT B7k</a>
    <a href="#">WHAT WE DO</a>
    <a href="#">LATEST NEWS</a>
    <a href="#">CONTACT US</a>
  </nav>
  <a class="btn btn-donate" href="#">DONATE</a>
</header>

<section class="hero" role="img" aria-label="Cyclists riding along a dirt road through green hills">
  <div class="hero-shade"></div>
  <h1 class="hero-title">Compass9Reach (B7k)</h1>
  <p class="hero-sub">Facilitating cross sector collaboration for social good. A service that advocates, unites and supports collaborative resilience to humanitarian crises</p>
  <a class="btn btn-hero" href="#">Learn More</a>
</section>

<section>
  <p class="abs welcome-kicker">Welcome to Compass9Reach</p>
  <h2 class="abs welcome-title">COLLABORATION FOR GOOD</h2>
  <p class="abs welcome-text">Based in Geneva, Switzerland – renowned as the world's humanitarian capital – B7k facilitates cross sector collaboration for social good. It was founded in response to the growing need for independent quality support for collaboration between different sectors of society attempting to achieve practical objectives of mutual interest.</p>
  <a class="abs welcome-link" href="#">Learn More &gt;&gt;</a>
</section>

<section class="volunteer-band" role="img" aria-label="Children laughing together while playing outdoors">
  <div class="overlay"></div>
</section>
<p class="abs kicker" style="top:862px">Can you help?</p>
<div class="abs kicker-rule" style="top:892px"></div>
<h2 class="abs volunteer-title">VOLUNTEERS NEEDED</h2>
<p class="abs volunteer-text">Want to take action or join a local campaign? Become a proud volunteer with KindHand!</p>
<a class="btn btn-signup" href="#">Sign Up</a>

<section>
  <h2 class="abs section-title">Latest News</h2>
  <div class="abs section-rule"></div>

  <article class="news-card" style="left:200px">
    <div class="thumb" role="img" aria-label="Runners' legs on a race course" style="background:linear-gradient(180deg,#6c7a86,#4e5860)"></div>
    <p class="date">NOVEMBER 2, 2018</p>
    <h3 class="title">L.A. Mud Race 2018</h3>
    <p class="excerpt">Add-in an option except to describe your event. This text will only display on the event listing page.</p>
    <div class="divider"></div>
    <a class="more" href="#">Read more</a>
  </article>

  <article class="news-card bordered" style="left:479px">
    <div class="thumb" role="img" aria-label="Volunteers in grey shirts gathered outdoors" style="background:linear-gradient(180deg,#8da070,#9a9a8c)"></div>
    <p class="date">NOVEMBER 15, 2018</p>
    <h3 class="title">Fundraising 10k Run</h3>
    <p class="excerpt">Add-in an option except to describe your event. This text will only display on the event listing page.</p>
    <div class="divider"></div>
    <a class="more" href="#">Read more</a>
  </article>

  <article class="news-card" style="left:753px">
    <div class="thumb" role="img" aria-label="Participants crawling through a muddy obstacle" style="background:linear-gradient(180deg,#6f8a5a,#8a7a5c)"></div>
    <p class="date">DECEMBER 7, 2018</p>
    <h3 class="title">Donate For The Children</h3>
    <p class="excerpt">Add-in an option except to describe your event. This text will only display on the event listing page.</p>
    <div class="divider"></div>
    <a class="more" href="#">Read more</a>
  </article>
</section>

<section class="gallery">
  <div class="tile" role="img" aria-label="Mud obstacle race" style="background:linear-gradient(180deg,#6f7a5a,#8a7458)"></div>
  <div class="tile" role="img" aria-label="Runners on the road" style="background:linear-gradient(180deg,#8a6a6a,#6a7078)"></div>
  <div class="tile" role="img" aria-label="Water slide obstacle" style="background:linear-gradient(180deg,#3a8a8a,#5fb0a8)"></div>
  <div class="tile" role="img" aria-label="Racers after a muddy course" style="background:linear-gradient(180deg,#5a5a4e,#3e3a36)"></div>
  <div class="tile" role="img" aria-label="Climbing rope close-up" style="background:linear-gradient(180deg,#9a8a7a,#c8c0b4)"></div>
  <div class="tile" role="img" aria-label="Swimmers entering the sea" style="background:linear-gradient(180deg,#4a6a7a,#8aa0aa)"></div>
</section>
<a class="to-top" href="#" aria-label="Back to top">
  <svg width="32" height="32" viewBox="0 0 32 32"><path d="M11 18 L16 13 L21 18" fill="none" stroke="#fff" stroke-width="2"/></svg>
</a>

<section class="newsletter" role="img" aria-label="Children pulling a rope in a tug of war">
  <div class="overlay"></div>
</section>
<h2 class="abs newsletter-title">Subscribe to our Newsletter</h2>
<p class="abs newsletter-text">Be the first one to hear our latest announcements, directly on your email.<br>Subscribe today and we will keep you up to date!</p>
<div class="signup-field">Your email address</div>
<a class="btn signup-btn" href="#">SIGN UP</a>

<footer class="site-footer"></footer>
<span class="footer-dot"></span>
<p class="abs footer-name">Compass9Reach</p>
<div class="footer-col" style="left:511px">
  <h4>Quick Link</h4>
  <ul>
    <li class="is-current">Home</li>
    <li>About B7k</li>
    <li>What We Do</li>
    <li>Latest News</li>
    <li>Contact Us</li>
  </ul>
</div>
<div class="footer-col" style="left:664px">
  <h4>Privacy</h4>
  <ul>
    <li>Privacy Policy</li>
    <li>Terms of Use</li>
    <li>FAQs</li>
  </ul>
</div>
<div class="footer-col" style="left:829px">
  <h4>Social</h4>
</div>
<div class="social" aria-label="Social links"><span></span><span></span><span></span><span></span></div>
<p class="abs copyright">Copyright 2018. <b>Compass9Reach</b>. All rights reserved.</p>

</body>
</html>
```